Locksmith Store 474747 Signage

Design Brief: Locksmith Store Signage – "Locksmith 474747" [ΚΛΕΙΔΑΡΑΣ 474747 (in Greek)]
We are looking for a spectacular and professional sign design for the exterior of our locksmith store.
Signage Dimensions:
• Width: 6 meters
• Height: 1.5 meters
• Shopfront window Width: 6 meters, Height: 2.5 meters
Key Requirements (in order of importance):
1. It must be immediately clear that this is a locksmith store. [ΚΛΕΙΔΑΡΑΣ (in Greek)]
2. The store name "474747", (which is also the phone number 2310474747), should be highly visible and visually striking because this is the number that customers are calling when they are locked out.
3. The signage should also clearly communicate that except for house keys, which is obvious for a locksmith store the services we provide are:
o All kinds of house keys. ΚΛΕΙΔΙΑ ΣΠΙΤΙΩΝ(in Greek) (There is no key that we cannot do)
o Immobiliser car keys = ΚΛΕΙΔΙΑ ΑΥΤΟΚΙΝΗΤΩΝ (in Greek)
We unlock every car that exist, we program new immobilizer keys – remote controls, even if all keys are lost, we repair or change broken cells of car keys, we change batteries.
o High-security locks = ΚΛΕΙΔΑΡΙΕΣ ΑΣΦΑΛΕΙΑΣ (in Greek) we sell the best high security locks in the planet
o Armoured doors = ΠΟΡΤΕΣ ΑΣΦΑΛΕΙΑΣ (in Greek) (this may not be so important to be on the signage.
Visual Style:
We are open to creative direction, but the design should be eye-catching, professional, and modern, something that will stand out on a busy street and instantly tell customers who we are and what we offer. Also, you may use the shopfront window for graphic designs. Also, we are open if a part of the signage is digital.
________________________________________
Updates
Hello Designers,
Thank you so much for your effort and the designs you've shared.
I realized I forgot to mention that you can refer to my website at www.474747-keys.example.gr for more context.
Additionally, I’ve just uploaded two new photos: one showing the store with a black outline at the dimensions of the signage, and another with the large double-bit key placed in a different position to demonstrate that it is moveable.
Thanks again for your dedication!
Target Market(s)
every person that has a key
Look and feel
Each slider illustrates characteristics of the customer's brand and the style your logo design should communicate.

```html
<!DOCTYPE html>
<html lang="el">
<head>
<meta charset="utf-8">
<title>ΚΛΕΙΔΑΡΑΣ 474747 – Signage</title>
<link rel="stylesheet" href="https://fonts.googleapis.com/css2?family=Noto+Sans:wght@400;500&family=Rubik:wght@800;900&display=swap">
<style>
  :root{
    --page:#c6c6c6;
    --sign-black:#050505;
    --sign-dark:#1b1b1b;
    --red:#f0141b;
    --white:#ffffff;
    --gold-1:#ffc21a;
    --gold-2:#ffe27a;
    --gold-3:#b98a12;
    --ink:#0a0a0a;
  }
  *{margin:0;padding:0;box-sizing:border-box}
  html,body{width:1200px;height:925px;overflow:hidden;background:var(--page)}
  body{position:relative;font-family:"Noto Sans",Arial,sans-serif}

  .sign{position:absolute;left:87px;width:1014px;overflow:hidden;
    background:linear-gradient(90deg,var(--sign-black) 0%,var(--sign-black) 55%,var(--sign-dark) 100%)}
  .sign--wide{top:75px;height:423px}
  .sign--compact{top:560px;height:253px}

  .sign__artwork{position:absolute;top:0;right:0;bottom:0;
    background:
      radial-gradient(ellipse at 80% 25%,rgba(230,180,40,.55) 0%,rgba(120,90,20,.25) 30%,transparent 60%),
      radial-gradient(ellipse at 45% 60%,#8d8d8d 0%,#4a4a4a 25%,transparent 55%),
      linear-gradient(90deg,transparent 0%,#1a1a1a 30%,#202020 100%)}
  .sign--wide .sign__artwork{width:330px}
  .sign--compact .sign__artwork{width:230px}

  .sign__name{position:absolute;color:var(--white);font-weight:400;letter-spacing:1px;line-height:1;white-space:nowrap}
  .sign__number{position:absolute;color:var(--red);font-family:"Rubik",Arial,sans-serif;font-weight:900;line-height:1;letter-spacing:1px;white-space:nowrap}

  .sign--wide .sign__name{left:47px;top:56px;font-size:66px}
  .sign--wide .sign__number{left:413px;top:50px;font-size:82px}
  .sign--compact .sign__name{left:43px;top:38px;font-size:64px}
  .sign--compact .sign__number{left:43px;top:90px;font-size:76px;letter-spacing:2px}

  .phone-band{position:absolute;left:0;bottom:0;
    background:linear-gradient(90deg,var(--gold-1) 0%,var(--gold-1) 45%,var(--gold-2) 75%,var(--gold-3) 100%)}
  .sign--wide .phone-band{height:86px;width:451px;clip-path:polygon(0 0,418px 0,451px 100%,0 100%)}
  .sign--compact .phone-band{height:75px;width:457px;clip-path:polygon(0 0,429px 0,457px 100%,0 100%)}
  .phone-band__icon{position:absolute;width:30px;height:30px}
  .phone-band__number{position:absolute;font-family:"Rubik",Arial,sans-serif;font-weight:900;color:var(--ink);line-height:1;font-size:46px;letter-spacing:-0.5px;white-space:nowrap}
  .sign--wide .phone-band__icon{left:34px;top:28px}
  .sign--wide .phone-band__number{left:85px;top:20px}
  .sign--compact .phone-band__icon{left:44px;top:22px}
  .sign--compact .phone-band__number{left:95px;top:15px}

  .services{position:absolute;list-style:none}
  .service{position:absolute;display:flex;align-items:center}
  .service__badge{flex:none;border-radius:50%;background:var(--white);border:3px solid var(--red);display:flex;align-items:center;justify-content:center}
  .service__label{color:var(--white);line-height:1;text-transform:uppercase;white-space:nowrap}

  .sign--wide .service__badge{width:60px;height:60px;margin-right:14px}
  .sign--wide .service__badge svg{width:34px;height:34px}
  .sign--wide .service__label{font-size:27px}
  .sign--compact .service__badge{width:44px;height:44px;margin-right:10px}
  .sign--compact .service__badge svg{width:26px;height:26px}
  .sign--compact .service__label{font-size:19px}

  .brand-mark{position:absolute;color:var(--white);font-weight:500;line-height:1;white-space:nowrap}
  .sign--wide .brand-mark{left:489px;top:350px;font-size:28px}
  .sign--compact .brand-mark{left:529px;top:194px;font-size:24px}
</style>
</head>
<body>

<svg width="0" height="0" style="position:absolute" aria-hidden="true">
  <defs>
    <symbol id="icon-keys" viewBox="0 0 24 24"><circle cx="8" cy="8" r="4.5" fill="none" stroke="#111" stroke-width="2.4"/><path d="M11 11l8 8m-3-3l2-2m-4 0l2-2" stroke="#111" stroke-width="2.4" fill="none" stroke-linecap="round"/></symbol>
    <symbol id="icon-car" viewBox="0 0 24 24"><circle cx="7" cy="5" r="2.5" fill="none" stroke="#111" stroke-width="2"/><path d="M9.5 5h9" stroke="#111" stroke-width="2"/><path d="M4 17v-4l2-4h12l2 4v4z" fill="#111"/><circle cx="7.5" cy="14" r="1.3" fill="#fff"/><circle cx="16.5" cy="14" r="1.3" fill="#fff"/><rect x="5" y="17" width="3" height="3" fill="#111"/><rect x="16" y="17" width="3" height="3" fill="#111"/></symbol>
    <symbol id="icon-shield" viewBox="0 0 24 24"><circle cx="12" cy="12" r="10" fill="none" stroke="#111" stroke-width="1.8"/><path d="M12 4l6 2.5v5c0 4-3 6.5-6 8-3-1.5-6-4-6-8v-5z" fill="#111"/><rect x="9.5" y="11" width="5" height="4" fill="#fff"/><path d="M10.5 11V9.5a1.5 1.5 0 013 0V11" stroke="#fff" stroke-width="1.2" fill="none"/></symbol>
    <symbol id="icon-door" viewBox="0 0 24 24"><rect x="5" y="3" width="8" height="18" rx="1.5" fill="#111"/><path d="M9 8h11" stroke="#111" stroke-width="3" stroke-linecap="round"/><circle cx="9" cy="8" r="1.6" fill="#fff"/><rect x="8.2" y="13" width="1.6" height="4" fill="#fff"/></symbol>
    <symbol id="icon-phone" viewBox="0 0 24 24"><path d="M6.6 10.8a15 15 0 006.6 6.6l2.2-2.2c.3-.3.7-.4 1-.2 1.1.4 2.3.6 3.6.6.6 0 1 .4 1 1V20c0 .6-.4 1-1 1A17 17 0 013 4c0-.6.4-1 1-1h3.5c.6 0 1 .4 1 1 0 1.3.2 2.5.6 3.6.1.4 0 .7-.2 1z" fill="#0a0a0a"/><path d="M14 3a7 7 0 017 7M14 6.5a3.5 3.5 0 013.5 3.5" stroke="#0a0a0a" stroke-width="1.8" fill="none" stroke-linecap="round"/></symbol>
  </defs>
</svg>

<section class="sign sign--wide">
  <div class="sign__artwork" role="img" aria-label="Golden key turning in a silver puzzle-piece keyhole on a dark puzzle background"></div>
  <h1 class="sign__name">ΚΛΕΙΔΑΡΑΣ</h1>
  <p class="sign__number">474747</p>

  <ul class="services">
    <li class="service" style="left:50px;top:146px"><span class="service__badge"><svg><use href="#icon-keys"/></svg></span><span class="service__label">ΚΛΕΙΔΙΑ<br>ΣΠΙΤΙΩΝ</span></li>
    <li class="service" style="left:322px;top:146px"><span class="service__badge"><svg><use href="#icon-car"/></svg></span><span class="service__label">ΚΛΕΙΔΙΑ<br>ΑΥΤΟΚΙΝΗΤΩΝ</span></li>
    <li class="service" style="left:50px;top:229px"><span class="service__badge"><svg><use href="#icon-shield"/></svg></span><span class="service__label">ΚΛΕΙΔΑΡΙΕΣ<br>ΑΣΦΑΛΕΙΑΣ</span></li>
    <li class="service" style="left:322px;top:233px"><span class="service__badge"><svg><use href="#icon-door"/></svg></span><span class="service__label">ΠΟΡΤΕΣ<br>ΑΣΦΑΛΕΙΑΣ</span></li>
  </ul>

  <div class="phone-band">
    <svg class="phone-band__icon"><use href="#icon-phone"/></svg>
    <span class="phone-band__number">2310474747</span>
  </div>

  <span class="brand-mark">ΚΛΕΙΔΑΡΑΣ 474747</span>
</section>

<section class="sign sign--compact">
  <div class="sign__artwork" role="img" aria-label="Golden key in a silver puzzle-piece keyhole with warm glow"></div>
  <h2 class="sign__name">ΚΛΕΙΔΑΡΑΣ</h2>
  <p class="sign__number">474747</p>

  <ul class="services">
    <li class="service" style="left:445px;top:46px"><span class="service__badge"><svg><use href="#icon-keys"/></svg></span><span class="service__label">ΚΛΕΙΔΙΑ<br>ΣΠΙΤΙΩΝ</span></li>
    <li class="service" style="left:623px;top:46px"><span class="service__badge"><svg><use href="#icon-car"/></svg></span><span class="service__label">ΚΛΕΙΔΙΑ<br>ΑΥΤΟΚΙΝΗΤΩΝ</span></li>
    <li class="service" style="left:445px;top:108px"><span class="service__badge"><svg><use href="#icon-shield"/></svg></span><span class="service__label">ΚΛΕΙΔΑΡΙΕΣ<br>ΑΣΦΑΛΕΙΑΣ</span></li>
    <li class="service" style="left:623px;top:108px"><span class="service__badge"><svg><use href="#icon-door"/></svg></span><span class="service__label">ΠΟΡΤΕΣ<br>ΑΣΦΑΛΕΙΑΣ</span></li>
  </ul>

  <div class="phone-band">
    <svg class="phone-band__icon"><use href="#icon-phone"/></svg>
    <span class="phone-band__number">2310474747</span>
  </div>

  <span class="brand-mark">ΚΛΕΙΔΑΡΑΣ 474747</span>
</section>

</body>
</html>
```